Business card design for an Art Director working for museums

The business card design we're looking for is for an Art Director in a private museum called "OLV Gallery". The museum showcases artworks made by the country's national artists. Designs should use the CMYK "0 40 100 20". You have the liberty to use any type you want except for overly decorative ones.

Target Market(s)

Professional and creative individuals. Interior designers, museum curators, museum coordinators etc

Industry/Entity Type

Museum

Contact Information for Business Card

Rina T
Art Director
+1 555 374 9281

Font styles to use
Serif
Sans Serif
Script

Requirements
Must have
• My project must have the CMYK 0 40 100 20. You can play with the Key.
• We're keen on clean, minimal, and architectural-type design.
Nice to have
• Geometric gradients that nicely complement the main CMYK that we've posted.
Should not have
• Off-putting colour palettes

```html
<!DOCTYPE html>
<html lang="en">
<head>
<meta charset="utf-8">
<title>Rina T — Business Card</title>
<link href="https://fonts.googleapis.com/css2?family=Great+Vibes&family=PT+Sans:ital@0;1&display=swap" rel="stylesheet">
<style>
  :root {
    --gold: #d08a2e;
    --gold-deep: #c8702e;
    --paper: #f4f4f4;
    --stage-light: #ffffff;
    --stage-dark: #363435;
    --ink: #333333;
  }
  * { margin: 0; padding: 0; box-sizing: border-box; }
  html, body { width: 1200px; height: 1000px; overflow: hidden; }
  body { position: relative; background: var(--stage-light); font-family: "PT Sans", sans-serif; }
  .stage-lower { position: absolute; left: 0; top: 500px; width: 1200px; height: 500px; background: var(--stage-dark); }
  .card {
    position: absolute; left: 250px; width: 698px; height: 434px;
    border: 9px solid var(--gold); border-radius: 30px;
    background: var(--paper); overflow: hidden;
  }
  .card-front { top: 33px; }
  .card-back { top: 533px; }
  .holder-name {
    position: absolute; left: 18px; top: 16px;
    font-family: "Great Vibes", cursive; font-size: 118px; line-height: 1;
    color: var(--gold); white-space: nowrap;
  }
  .brand {
    position: absolute; display: flex; align-items: center; gap: 8px;
    font-family: "PT Sans", sans-serif; white-space: nowrap; line-height: 1.2;
  }
  .brand-mark { display: block; flex-shrink: 0; background: currentColor; }
  .brand-small { left: 98px; top: 192px; width: 200px; justify-content: center; font-size: 22px; color: var(--gold); }
  .brand-small .brand-mark { width: 13px; height: 13px; }
  .details { position: absolute; left: 48px; top: 256px; width: 300px; text-align: center; }
  .role { font-size: 22px; color: var(--gold-deep); line-height: 1.1; }
  .company { font-size: 33px; color: var(--gold-deep); line-height: 1.1; }
  .phone { margin-top: 10px; font-size: 33px; font-style: italic; color: var(--gold); letter-spacing: 1px; }
  .page-curl { position: absolute; left: 0; top: 0; width: 680px; height: 416px; }
  .brand-curl { left: 473px; top: 300px; width: 220px; justify-content: center; font-size: 30px; color: var(--ink); }
  .brand-curl .brand-mark { width: 16px; height: 16px; }
  .brand-centre { left: 0; top: 184px; width: 680px; justify-content: center; font-size: 40px; color: var(--gold); }
  .brand-centre .brand-mark { width: 22px; height: 22px; }
</style>
</head>
<body>
  <div class="stage-lower"></div>

  <section class="card card-front">
    <div class="holder-name">Rina T</div>
    <div class="brand brand-small"><span class="brand-mark"></span>OLV Gallery</div>
    <div class="details">
      <p class="role">ART DIRECTOR</p>
      <p class="company">OLV GALLERY</p>
      <p class="phone">+1 555 374 9281</p>
    </div>
    <svg class="page-curl" viewBox="0 0 680 416" aria-hidden="true">
      <defs>
        <linearGradient id="curl-face" x1="420" y1="380" x2="680" y2="90" gradientUnits="userSpaceOnUse">
          <stop offset="0" stop-color="#ecebe4"/>
          <stop offset="0.35" stop-color="#d6d3c2"/>
          <stop offset="0.6" stop-color="#3e3d35"/>
          <stop offset="0.78" stop-color="#a8a58c"/>
          <stop offset="1" stop-color="#e2e0d3"/>
        </linearGradient>
      </defs>
      <path d="M300,416 C360,400 395,330 400,250 C403,190 405,150 410,143 C520,140 640,120 670,70 L680,40 L680,416 Z" fill="url(#curl-face)"/>
      <path d="M300,416 C360,400 395,330 400,250 C403,190 405,150 410,143" fill="none" stroke="#bdbaa8" stroke-width="1"/>
    </svg>
    <div class="brand brand-curl"><span class="brand-mark"></span>OLV Gallery</div>
  </section>

  <section class="card card-back">
    <div class="brand brand-centre"><span class="brand-mark"></span>OLV Gallery</div>
  </section>
</body>
</html>
```